依頼詳細
おおよそのイメージは添付した他店ポスターです。¥2,980から飲み放題付きで宴会ができるという事をおすすめ。料理は¥2,500コースをおすすめしたい。(11月末に2号店オープンのため()の文字も入れ替えられるようにデザインお願いします)
記載項目
飲み放題付き
忘新年会宴会コース

おひとり様¥2,980から
(おひとり様¥3,480から)

2〜25名様まで
(2〜40名様まで)

¥2,500コース 全9品
付出し
塩だれキャベツ
おすすめ鮮魚の一品
名古屋手羽先
鶏ちゃん焼き
〆のきしめん
みそ串かつ
とうふの和風サラダ
デザート

¥2,000コース 全7品
付出し
塩だれキャベツ
名古屋手羽先
鶏ちゃん焼き
〆のきしめん
みそ串かつ
とうふの和風サラダ

飲み放題 全60種類
2時間(ラストオーダーは30分前) おひとり様 +¥980
2.5時間(ラストオーダーは30分前) おひとり様 +¥1,480

ご予約受付 076-395-1847
(076-318-7502)
サイズ
A2サイズ
ページ数
片面
希望イメージ
シンプル 複雑
単色 カラフル
暗い 明るい
日常 高級
遊び心 厳粛
未来的 伝統的
女性的 男性的
希望する色
オレンジ 金 黒
納品ファイル
• 高解像度JPG (.jpg)
• イラストレーター形式 (.ai)
補足説明
当店のサイトページです。 http://www.kurumiza.jp/strK004719386/
コース画像、ロゴ、素材追加します。
コース写真の追加です。
コース写真の縦サイズ追加します。この写真の方が良いかもしれません。

訴求ポイントの見やすさなどが選んだ理由です。その他のデザインもホントよかったのですがこちらに決めさせていただきました。

たくさん提案ありがとうございました。今後もいろいろデザインお願いする事があると思いますが宜しくお願いいたします。

```html
<!DOCTYPE html>
<html lang="ja">
<head>
<meta charset="utf-8">
<title>忘・新年会宴会 飲み放題付き</title>
<link href="https://fonts.googleapis.com/css2?family=Dela+Gothic+One&family=M+PLUS+Rounded+1c:wght@500;700;800&display=swap" rel="stylesheet">
<style>
  :root{
    --paper:#ffffff;
    --ink:#2b201c;
    --gold:#c6a46a;
    --gold-light:#d9bd86;
    --red:#d71920;
    --white:#ffffff;
    --photo-a:#8a5a32;
    --photo-b:#c98a4e;
    --photo-c:#5b3a24;
  }
  *{margin:0;padding:0;box-sizing:border-box}
  html,body{width:882px;height:1200px;overflow:hidden;background:var(--paper)}
  body{font-family:"M PLUS Rounded 1c",sans-serif}
  .poster{position:relative;width:882px;height:1200px;background:var(--paper)}
  .sheet{position:absolute;left:35px;top:24px;width:812px;height:1148px;background:var(--ink);overflow:hidden}
  .course-photo{position:absolute;left:0;top:0;width:675px;height:600px;
    background:radial-gradient(ellipse at 35% 45%,var(--photo-b) 0%,var(--photo-a) 45%,var(--photo-c) 100%)}
  .side-banner{position:absolute;left:680px;top:10px;width:130px;height:780px;
    writing-mode:vertical-rl;font-family:"Dela Gothic One",sans-serif;font-size:118px;line-height:130px;
    color:var(--gold);letter-spacing:-6px;white-space:nowrap;text-align:start}
  .side-stop{position:absolute;left:680px;top:770px;width:130px;text-align:center;
    font-family:"Dela Gothic One",sans-serif;font-size:118px;line-height:118px;color:var(--gold)}
  .price-burst{position:absolute;left:430px;top:325px;width:260px;height:150px}
  .price-burst svg{position:absolute;inset:0}
  .price-burst .label{position:absolute;left:102px;top:36px;color:var(--white);font-weight:700;font-size:16px}
  .price-burst .amount{position:absolute;left:62px;top:56px;color:var(--white);font-weight:800;font-size:46px;letter-spacing:-1px;white-space:nowrap}
  .price-burst .amount small{font-size:22px}
  .price-burst .amount .from{font-size:18px}
  .title{position:absolute;left:30px;top:505px;width:640px;text-align:center;
    font-family:"Dela Gothic One",sans-serif;font-size:70px;line-height:1;color:var(--red);
    -webkit-text-stroke:14px var(--white);paint-order:stroke fill;transform:rotate(-2deg);letter-spacing:-2px}
  .band{position:absolute;left:0;top:590px;width:675px;height:66px;background:var(--red);
    font-family:"Dela Gothic One",sans-serif;font-size:50px;line-height:66px;color:var(--gold-light);
    text-align:center;padding-left:40px;letter-spacing:2px}
  .course{position:absolute;top:696px;color:var(--gold)}
  .course.basic{left:45px}
  .course.premium{left:372px}
  .course-head{display:flex;align-items:center;gap:6px;height:40px}
  .thumb{width:42px;height:40px}
  .pill{background:var(--gold);color:var(--ink);font-weight:800;border-radius:20px;height:30px;line-height:30px;font-size:21px;padding:0 12px}
  .pill small{font-size:14px}
  .pill.count{width:44px;height:34px;line-height:34px;border-radius:50%;padding:0;text-align:center;font-size:20px}
  .course ol{list-style:none;margin-top:20px;margin-left:8px}
  .course li{font-size:23px;font-weight:700;line-height:31px;white-space:nowrap}
  .course li span{display:inline-block;width:38px}
  .drink-note{position:absolute;right:14px;top:1020px;color:var(--white);font-size:9px;line-height:12px;font-weight:500;white-space:pre;text-align:left}
  .brand{position:absolute;left:60px;top:1050px;color:var(--gold)}
  .brand .tag{font-size:15px;font-weight:800;margin-left:170px;letter-spacing:2px}
  .brand .name{display:flex;align-items:center;gap:10px;font-size:46px;font-weight:800;line-height:56px}
  .brand .dot{width:34px;height:34px;border-radius:50%;background:var(--gold)}
  .reserve{position:absolute;left:552px;top:1062px;width:246px}
  .reserve .bar{background:var(--gold);color:var(--red);font-weight:800;font-size:18px;text-align:center;height:26px;line-height:26px}
  .reserve .tel{color:var(--gold);font-weight:800;font-size:34px;line-height:40px;margin-top:6px;letter-spacing:-1px;white-space:nowrap}
</style>
</head>
<body>
<div class="poster">
  <div class="sheet">
    <div class="course-photo" role="img" aria-label="名古屋手羽先と鍋料理などの宴会コース料理の写真"></div>

    <div class="side-banner">ご予約承り中</div>
    <div class="side-stop">。</div>

    <div class="price-burst">
      <svg viewBox="0 0 260 150" width="260" height="150" aria-hidden="true">
        <polygon fill="var(--red)" points="10,78 50,60 30,30 85,40 100,8 130,32 165,5 175,38 230,22 215,55 255,70 222,90 248,125 195,112 180,145 145,118 110,140 95,112 45,128 55,100"/>
      </svg>
      <div class="label">おひとり様</div>
      <div class="amount"><small>¥</small>2,980<span class="from">から</span></div>
    </div>

    <div class="title">忘・新年会宴会</div>
    <div class="band">飲み放題付き</div>

    <section class="course basic">
      <div class="course-head">
        <svg class="thumb" viewBox="0 0 42 40" aria-hidden="true"><path fill="var(--gold)" d="M2 18h9v20H2zM13 18l8-14c3-3 7 0 6 4l-2 8h12c3 0 4 3 3 5l-4 15c-1 2-2 2-4 2H13z"/></svg>
        <div class="pill"><small>¥</small>2,000<small>コース</small></div>
        <div class="pill count">7<small>品</small></div>
      </div>
      <ol>
        <li><span>①</span>付出し</li>
        <li><span>②</span>塩だれキャベツ</li>
        <li><span>③</span>名古屋手羽先</li>
        <li><span>④</span>鶏ちゃん焼き</li>
        <li><span>⑤</span>〆のきしめん</li>
        <li><span>⑥</span>みそ串かつ</li>
        <li><span>⑦</span>とうふの和風サラダ</li>
      </ol>
    </section>

    <section class="course premium">
      <div class="course-head">
        <svg class="thumb" viewBox="0 0 42 40" aria-hidden="true"><path fill="var(--gold)" d="M2 18h9v20H2zM13 18l8-14c3-3 7 0 6 4l-2 8h12c3 0 4 3 3 5l-4 15c-1 2-2 2-4 2H13z"/></svg>
        <div class="pill"><small>¥</small>2,500<small>コース</small></div>
        <div class="pill count">9<small>品</small></div>
      </div>
      <ol>
        <li><span>①</span>付出し</li>
        <li><span>②</span>塩だれキャベツ</li>
        <li><span>③</span>おすすめ鮮魚の一品</li>
        <li><span>④</span>名古屋手羽先</li>
        <li><span>⑤</span>鶏ちゃん焼き</li>
        <li><span>⑥</span>〆のきしめん</li>
        <li><span>⑦</span>みそ串かつ</li>
        <li><span>⑧</span>とうふの和風サラダ</li>
        <li><span>⑨</span>デザート</li>
      </ol>
    </section>

    <div class="drink-note">●飲み放題　全60種類
　　2時間(ラストオーダーは30分前) おひとり様+¥　980
　2.5時間(ラストオーダーは30分前) おひとり様+¥1,480</div>

    <div class="brand">
      <div class="tag">名古屋手羽先</div>
      <div class="name"><span class="dot"></span>こがね酒場</div>
    </div>

    <div class="reserve">
      <div class="bar">ご予約受付</div>
      <div class="tel">076-395-1847</div>
    </div>
  </div>
</div>
</body>
</html>
```